Brochure design

We need a 4 page A4 brochure for our engieering companyA draft version of the text can be found in the attachments, along with the logo.The text pdf shows the general style and layout of hte text, but am very open to artistic advice.Three image placeholders should be added on pages indicated - these are not yet availableThe logo gives a good idea of the colour scheme required.For background graphics, the use of swirl patterns is desirable.Look and feel should be clean and professional, not too cluttered.Final desing shoul dbe avialable in RGB psd format, with full layers so we can modify text and images easily.

```html
<!DOCTYPE html>
<html lang="en">
<head>
<meta charset="utf-8">
<title>Northvale Thermal Engineering – Brochure Page</title>
<link href="https://fonts.googleapis.com/css2?family=Noto+Sans:wght@400;700&display=swap" rel="stylesheet">
<style>
  :root {
    --brand-blue: #0a4fa3;
    --brand-teal: #12a88a;
    --brand-grey: #8a8a8a;
    --text-dark: #333333;
    --paper: #ffffff;
  }
  * { margin: 0; padding: 0; box-sizing: border-box; }
  html, body { width: 848px; height: 1200px; overflow: hidden; background: var(--paper); }
  body { font-family: "Noto Sans", Verdana, sans-serif; color: var(--text-dark); }
  .page { position: relative; width: 848px; height: 1200px; overflow: hidden; background: var(--paper); }

  .swirl-wash {
    position: absolute; left: 80px; top: 150px; width: 768px; height: 610px;
    background:
      radial-gradient(circle at 28% 40%, rgba(10,79,163,0.07) 0, rgba(10,79,163,0.07) 22%, transparent 40%),
      radial-gradient(circle at 88% 60%, rgba(18,168,138,0.09) 0, rgba(18,168,138,0.09) 18%, transparent 34%),
      radial-gradient(circle at 55% 100%, rgba(138,138,138,0.07) 0, transparent 35%);
  }

  .rule { position: absolute; }
  .rule--v { top: 0; height: 1200px; width: 6px; }
  .rule--h { left: 0; width: 848px; height: 6px; }
  .rule--blue { background: var(--brand-blue); }
  .rule--teal { background: var(--brand-teal); }
  .rule--grey { background: var(--brand-grey); }

  .brand { position: absolute; left: 88px; top: 30px; display: flex; align-items: center; gap: 10px; }
  .brand__dot { width: 22px; height: 22px; border-radius: 50%; background: var(--brand-blue); }
  .brand__name { font-size: 22px; font-weight: 700; color: var(--brand-blue); letter-spacing: 0.5px; line-height: 1.1; }

  .contact { position: absolute; top: 68px; height: 18px; display: flex; align-items: center; color: #fff; font-size: 13px; }
  .contact__tab { width: 20px; height: 18px; }
  .contact__icon { width: 26px; height: 26px; margin: 0 2px; background: #fff; }
  .contact__text { height: 18px; line-height: 18px; padding: 0 6px; white-space: nowrap; }
  .contact--web { left: 304px; }
  .contact--web .contact__tab, .contact--web .contact__text { background: var(--brand-blue); }
  .contact--mail { left: 554px; }
  .contact--mail .contact__tab, .contact--mail .contact__text { background: var(--brand-teal); }

  .content { position: absolute; left: 116px; top: 182px; width: 660px; }
  .intro { font-size: 17.5px; font-weight: 700; color: var(--brand-blue); line-height: 22px; margin-bottom: 24px; }
  .section-title { font-size: 19px; font-weight: 700; color: var(--brand-teal); line-height: 24px; margin-bottom: 4px; }
  .section-title--caps { text-transform: uppercase; }
  .bullets { list-style: none; font-size: 15px; line-height: 20px; margin-bottom: 20px; }
  .bullets li { position: relative; padding-left: 25px; margin-bottom: 7px; }
  .bullets li::before {
    content: ""; position: absolute; left: 8px; top: 6px; width: 8px; height: 8px;
    background: var(--brand-teal); transform: rotate(45deg);
  }
  .closing { font-size: 15.5px; color: var(--brand-blue); line-height: 20.5px; margin-top: 28px; }

  .diagram-frame { position: absolute; left: 86px; top: 758px; width: 750px; height: 428px; border: 2px solid #000; background: #fff; padding: 10px; }
  .diagram-frame__fill { width: 100%; height: 100%; background: linear-gradient(135deg, #eef2f6 0%, #dfe9e2 50%, #e9ecef 100%); }
</style>
</head>
<body>
<main class="page">
  <div class="swirl-wash" role="img" aria-label="Soft swirl pattern background in blue, teal and grey"></div>

  <div class="rule rule--v rule--blue" style="left:25px"></div>
  <div class="rule rule--v rule--teal" style="left:44px"></div>
  <div class="rule rule--v rule--grey" style="left:65px"></div>
  <div class="rule rule--h rule--blue" style="top:110px"></div>
  <div class="rule rule--h rule--teal" style="top:130px"></div>
  <div class="rule rule--h rule--grey" style="top:150px"></div>

  <header>
    <div class="brand">
      <span class="brand__dot"></span>
      <span class="brand__name">NORTHVALE<br>THERMAL</span>
    </div>
    <div class="contact contact--web">
      <span class="contact__tab"></span>
      <svg class="contact__icon" viewBox="0 0 26 26" aria-hidden="true">
        <circle cx="13" cy="13" r="11" fill="none" stroke="#0a4fa3" stroke-width="2"/>
        <ellipse cx="13" cy="13" rx="5" ry="11" fill="none" stroke="#0a4fa3" stroke-width="1.5"/>
        <path d="M2 13h22M4 7h18M4 19h18" stroke="#0a4fa3" stroke-width="1.5"/>
      </svg>
      <span class="contact__text">www.northvale-thermal.co.uk</span>
    </div>
    <div class="contact contact--mail">
      <span class="contact__tab"></span>
      <svg class="contact__icon" viewBox="0 0 26 26" aria-hidden="true">
        <rect x="2" y="5" width="22" height="16" fill="#fff" stroke="#12a88a" stroke-width="2"/>
        <path d="M2 5l11 9 11-9" fill="none" stroke="#12a88a" stroke-width="2"/>
      </svg>
      <span class="contact__text">sam.reid@northvale-thermal.co.uk</span>
    </div>
  </header>

  <section class="content">
    <p class="intro">Northvale Thermal Engineering is a thermal engineering company specialising in the thermal management of electrical machines and electronic systems.</p>

    <h2 class="section-title">We are pleased to offer the following services:</h2>
    <ul class="bullets">
      <li>Design and consultancy</li>
      <li>Development, implementation and support of our custom thermal simulation tools</li>
    </ul>

    <h2 class="section-title section-title--caps">Design and consultancy</h2>
    <ul class="bullets">
      <li>We provide effective thermal design solutions for electrical machines and electronic systems</li>
      <li>We cover every stage of a design for feasibility studies, from concept comparisons to design optimisation</li>
      <li>We can review and improve cooling systems for existing designs</li>
      <li>We work with our own specially developed toolset or with software of customers preference</li>
      <li>We offer CFD, thermal network modelling, simple analytical analysis</li>
    </ul>

    <p class="closing">We are excellent collaborators and able to work closely with design teams from different technical disciplines to deliver solutions optimised towards product requirements and specifications</p>
  </section>

  <figure class="diagram-frame">
    <div class="diagram-frame__fill" role="img" aria-label="Illustrated diagram of an electrical distribution network: transformer station, main LV switchboards, LV panel, motors and remote monitoring devices linked by green lines"></div>
  </figure>
</main>
</body>
</html>
```